Podcast covert art for startup show

I need podcast cover art that stands out and clearly says what the podcast is about: startup stories.

This is an example of Castrova cover art:
https://www.filebarnex.com/s/q4k8tmwpl2vbx9r/Castrova%202.png?dl=0

You can see how mine is looking blah on this page:
https://www.filebarnex.com/s/7h3jrdkqa5wzm2f/My%20podcast%20art%20doesn%27t%20stand%20out%20enough.png?dl=0

I need something that will get attention on a page that's full of other podcast covers and be easy to read.

SOMETHINGS THAT MIGHT HELP:

I love how easy it is to read the titles of these podcasts:
https://www.filebarnex.com/s/wpx6ghtmr0cqv84/easy%20to%20read%20titles.png?dl=0

I love how the logos of these podcasts are easy to read but they don't take much space:
https://www.filebarnex.com/s/5t2yfnbkd8jxe63/nice%20logo%20placement.png?dl=0

Target Market(s)

Successful software entrepreneurs

Industry/Entity Type

Startup

Font styles to use
Serif

Colors
00a990

Requirements
Must have
• I need it to include this:
• - This phrase: Startup Stories
• - My logo (keep it small, but readable)
• - My photo
• MY LOGO:
• http://talvoren.com/logo
• MY FAVORITE PHOTO OF MYSELF:
• https://vault.stormlake.net/open?id=0Xq7T_pwkr5bnHYmQZAaLPKKRw3
• You can edit my photo any way you want, including removing the background, turning me into a black&white photo, etc
• OTHER PHOTOS OF ME:
• https://vault.stormlake.net/open?id=0Xq7T_pwkr5bnW8JdvqXAcMbPZN
• Castrova asks that the size be 3000 x 3000 pixels
Nice to have
• I prefer that it have have 1 dominating color to help it stand out.
• This is what I mean:
• https://www.filebarnex.com/s/q4k8tmwpl2vbx9r/Castrova%20-%20one%20dominating%20color.png?dl=0
• I really like this color:
• https://www.filebarnex.com/s/k9v1wfzhr3ndy7c/color%20I%20like.png?dl=0

```html
<!DOCTYPE html>
<html lang="en">
<head>
<meta charset="utf-8">
<title>Startup Stories — Podcast Cover</title>
<link rel="stylesheet" href="https://fonts.googleapis.com/css2?family=Alfa+Slab+One&family=Barlow+Semi+Condensed:wght@700&display=swap">
<style>
  :root {
    --brand-teal: #14a78e;
    --title-yellow: #f6ec1f;
    --label-navy: #1f2233;
    --label-text: #ffffff;
    --portrait-light: #8a8a8a;
    --portrait-dark: #222222;
  }
  html, body {
    margin: 0;
    padding: 0;
    width: 1200px;
    height: 1200px;
    overflow: hidden;
    background: var(--brand-teal);
  }
  .cover {
    position: relative;
    width: 1200px;
    height: 1200px;
    background: var(--brand-teal);
    overflow: hidden;
  }
  .host-photo {
    position: absolute;
    left: 450px;
    top: 0;
    width: 560px;
    height: 1200px;
    background: linear-gradient(180deg, var(--portrait-light) 0%, var(--portrait-dark) 100%);
  }
  .show-label {
    position: absolute;
    left: 127px;
    top: 126px;
    width: 286px;
    height: 86px;
    background: var(--label-navy);
    display: flex;
    align-items: center;
    justify-content: center;
    font-family: "Barlow Semi Condensed", "Arial Narrow", sans-serif;
    font-weight: 700;
    font-size: 50px;
    letter-spacing: 1px;
    color: var(--label-text);
  }
  .show-title {
    position: absolute;
    left: 0;
    top: 0;
    width: 1200px;
    height: 1200px;
  }
  .show-title text {
    font-family: "Alfa Slab One", "Rockwell", serif;
    font-size: 182px;
    fill: var(--title-yellow);
  }
</style>
</head>
<body>
  <main class="cover">
    <div class="host-photo" role="img" aria-label="Black and white photo of the host smiling and throwing a playful punch toward the viewer"></div>

    <div class="show-label">TALVOREN</div>

    <svg class="show-title" viewBox="0 0 1200 1200" aria-label="Startup Stories">
      <text x="129" y="899" textLength="951" lengthAdjust="spacingAndGlyphs">STARTUP</text>
      <text x="129" y="1058" textLength="951" lengthAdjust="spacingAndGlyphs">STORIES</text>
    </svg>
  </main>
</body>
</html>
```